Label Design for Amber Kettle Specialty Coffee Roasters

We are a specialty coffee beans Roasting Shop named "Amber Kettle". We pack our beans in stand up poaches of varying sizes. We sell beans both to B2C and B2B and are looking to design stickers that will stand out. Our logo was designed with a black and white background. So far, we have been using white glossy bean bags and came up with a front label design that we would like to use for our labels.
We would like to see the design tweaked to fit both a white bag and a black one.
Currently, the attached front label design does not work on white bags. We would also like to have a back sticker designed that needs to include: 1- a description section for the type of beans used 2- a QR code section

Target Market(s)

Specialty beans in our area are typically liked by the younger generations 40 years and younger. Both male and females drink our coffee with varying income levels. But generally, middle class and above buy our coffee beans.

Requirements
Must have
• We are am looking for a sticker to be placed on a coffee bean bag. The sticker needs to contain the roasting shop's logo and brand name "Amber Kettle". Also, the sticker needs to have the following: country name, bean variety, weight (kg), roast date. The sticker needs to have the following specifications on a 5 point Likert scale (Strength, Fruitiness, Earthiness, Brightness). I uploaded a front label design that needs to be tweaked to fit both a white bag and a black one. The current design has owls representing the 5 point Likert scale and part of the shop's logo. We would like to keep that part of the design if possible. Currently, the attached front label design does not work on white bags.
We would also like to have a back sticker designed that needs to include: 1- a description section for the type of beans used 2- a QR code section
Nice to have
• The font that is used in the logo is League Gothic. It is okay to use this font or any other font if you find it more appropriate for the design.

```html
<!DOCTYPE html>
<html lang="en">
<head>
<meta charset="utf-8">
<title>Amber Kettle Specialty Coffee Roasters – Front Labels</title>
<link rel="stylesheet" href="https://fonts.googleapis.com/css2?family=PT+Sans+Narrow:wght@400;700&display=swap">
<style>
  :root {
    --ink: #0b0b0b;
    --paper: #ffffff;
    --backdrop: #ececec;
    --muted-on-dark: #a9a9a9;
    --muted-on-light: #6f6f6f;
    --dot-off-light: #d4d4d4;
    --dot-off-dark: #4a4a4a;
    --art-light-a: #f6f6f6;
    --art-light-b: #d6d6d6;
    --art-dark-a: #161616;
    --art-dark-b: #3c3c3c;
  }
  * { box-sizing: border-box; margin: 0; padding: 0; }
  html, body { width: 1200px; height: 848px; overflow: hidden; }
  body {
    background: var(--backdrop);
    font-family: "PT Sans Narrow", "Arial Narrow", sans-serif;
    position: relative;
  }

  .label {
    position: absolute;
    top: 313px;
    width: 314px;
    height: 378px;
    overflow: hidden;
  }
  .label--for-black-bag { left: 144px; background: var(--paper); color: var(--paper); }
  .label--for-white-bag { left: 751px; background: var(--ink); color: var(--ink); }

  .label__art { position: absolute; inset: 0; }
  .label--for-black-bag .label__art {
    background:
      radial-gradient(ellipse 70px 60px at 20% 16%, var(--art-light-b), transparent 75%),
      radial-gradient(ellipse 60px 140px at 90% 38%, var(--art-light-b), transparent 75%),
      radial-gradient(ellipse 60px 90px at 10% 80%, var(--art-light-b), transparent 75%),
      var(--art-light-a);
  }
  .label--for-white-bag .label__art {
    background:
      radial-gradient(ellipse 70px 60px at 20% 16%, var(--art-dark-b), transparent 75%),
      radial-gradient(ellipse 60px 140px at 90% 38%, var(--art-dark-b), transparent 75%),
      radial-gradient(ellipse 60px 90px at 10% 80%, var(--art-dark-b), transparent 75%),
      var(--art-dark-a);
  }

  .brand {
    position: absolute;
    left: 107px; top: 20px;
    width: 108px; height: 85px;
    border-radius: 10px;
    display: flex; align-items: center; justify-content: center;
    font-weight: 700; font-size: 17px; line-height: 1.05;
    text-transform: uppercase; text-align: center;
  }
  .label--for-black-bag .brand { background: var(--ink); color: var(--paper); }
  .label--for-white-bag .brand { background: var(--paper); color: var(--ink); }

  .info {
    position: absolute;
    left: 26px; top: 122px;
    width: 261px; height: 232px;
    border-radius: 11px;
    text-align: center;
  }
  .label--for-black-bag .info { background: var(--ink); color: var(--paper); }
  .label--for-white-bag .info { background: var(--paper); color: var(--ink); }

  .info__rule {
    position: absolute; left: 10px; right: 10px; height: 0;
    border-top: 2px dotted currentColor; opacity: 0.5;
  }
  .info__rule--top { top: 12px; }
  .info__rule--bottom { bottom: 9px; }

  .origin {
    position: absolute; left: 0; right: 0; top: 22px;
    font-weight: 700; font-size: 19px; line-height: 1;
  }
  .variety {
    position: absolute; left: 0; right: 0; top: 44px;
    font-size: 14px; line-height: 1;
  }
  .label--for-black-bag .variety { color: var(--muted-on-dark); }
  .label--for-white-bag .variety { color: var(--muted-on-light); }

  .profile {
    position: absolute;
    left: 38px; top: 68px;
    width: 183px; height: 92px;
  }
  .profile__bg { position: absolute; inset: 0; width: 100%; height: 100%; }
  .profile__list {
    position: absolute; left: 0; right: 0; top: 9px;
    list-style: none;
  }
  .profile__row {
    display: flex; align-items: center; height: 18.5px;
    font-size: 14px; line-height: 1;
  }
  .profile__name { width: 86px; text-align: right; padding-right: 9px; }
  .profile__scale { display: flex; gap: 3px; }
  .dot { display: block; width: 9px; height: 9px; border-radius: 50%; }
  .label--for-black-bag .profile__row { color: var(--ink); }
  .label--for-black-bag .dot { background: var(--ink); }
  .label--for-black-bag .dot--off { background: var(--dot-off-light); }
  .label--for-white-bag .profile__row { color: var(--paper); }
  .label--for-white-bag .dot { background: var(--paper); }
  .label--for-white-bag .dot--off { background: var(--dot-off-dark); }

  .facts {
    position: absolute; left: 0; right: 0; top: 173px;
    height: 38px;
  }
  .fact { position: absolute; top: 0; line-height: 1; }
  .fact--weight { right: 144px; text-align: right; }
  .fact--date { left: 129px; text-align: left; }
  .facts__divider {
    position: absolute; left: 122px; top: 0; bottom: 0;
    border-left: 2px dotted currentColor; opacity: 0.8;
  }
  .fact__title { font-weight: 700; font-size: 13px; }
  .fact__value { font-size: 12px; margin-top: 6px; }
  .label--for-black-bag .fact__title { color: var(--muted-on-dark); }
  .label--for-white-bag .fact__title { color: var(--muted-on-light); }
</style>
</head>
<body>

  <section class="label label--for-black-bag" aria-label="Front label for black bag">
    <div class="label__art" role="img" aria-label="Engraved-style illustration of a coffee cup, beans and coffee plant branch in light grey"></div>
    <div class="brand">Amber<br>Kettle</div>
    <div class="info">
      <div class="info__rule info__rule--top"></div>
      <h1 class="origin">COLOMBIA</h1>
      <p class="variety">VARIETY</p>
      <div class="profile">
        <svg class="profile__bg" viewBox="0 0 183 92" preserveAspectRatio="none" aria-hidden="true">
          <rect x="0" y="0" width="183" height="92" rx="11" fill="#ffffff"/>
        </svg>
        <ul class="profile__list">
          <li class="profile__row"><span class="profile__name">STRENGHT</span><span class="profile__scale"><i class="dot"></i><i class="dot"></i><i class="dot"></i><i class="dot dot--off"></i><i class="dot dot--off"></i></span></li>
          <li class="profile__row"><span class="profile__name">FRUITINESS</span><span class="profile__scale"><i class="dot"></i><i class="dot dot--off"></i><i class="dot dot--off"></i><i class="dot dot--off"></i><i class="dot dot--off"></i></span></li>
          <li class="profile__row"><span class="profile__name">EARTHINESS</span><span class="profile__scale"><i class="dot"></i><i class="dot"></i><i class="dot"></i><i class="dot dot--off"></i><i class="dot dot--off"></i></span></li>
          <li class="profile__row"><span class="profile__name">BRIGHTNESS</span><span class="profile__scale"><i class="dot"></i><i class="dot"></i><i class="dot"></i><i class="dot dot--off"></i><i class="dot dot--off"></i></span></li>
        </ul>
      </div>
      <div class="facts">
        <div class="fact fact--weight"><div class="fact__title">WEIGHT</div><div class="fact__value">60 KG</div></div>
        <div class="facts__divider"></div>
        <div class="fact fact--date"><div class="fact__title">ROAST DATE</div><div class="fact__value">05/5/2021</div></div>
      </div>
      <div class="info__rule info__rule--bottom"></div>
    </div>
  </section>

  <section class="label label--for-white-bag" aria-label="Front label for white bag">
    <div class="label__art" role="img" aria-label="Engraved-style illustration of a coffee cup, beans and coffee plant branch in dark grey"></div>
    <div class="brand">Amber<br>Kettle</div>
    <div class="info">
      <div class="info__rule info__rule--top"></div>
      <h1 class="origin">COLOMBIA</h1>
      <p class="variety">VARIETY</p>
      <div class="profile">
        <svg class="profile__bg" viewBox="0 0 183 92" preserveAspectRatio="none" aria-hidden="true">
          <path d="M14 0 H172 Q183 0 183 11 V81 Q183 92 172 92 H20 Q10 92 9 82 L2 12 Q1 0 14 0 Z" fill="#0b0b0b"/>
        </svg>
        <ul class="profile__list">
          <li class="profile__row"><span class="profile__name">STRENGHT</span><span class="profile__scale"><i class="dot"></i><i class="dot"></i><i class="dot"></i><i class="dot dot--off"></i><i class="dot dot--off"></i></span></li>
          <li class="profile__row"><span class="profile__name">FRUITINESS</span><span class="profile__scale"><i class="dot"></i><i class="dot dot--off"></i><i class="dot dot--off"></i><i class="dot dot--off"></i><i class="dot dot--off"></i></span></li>
          <li class="profile__row"><span class="profile__name">EARTHINESS</span><span class="profile__scale"><i class="dot"></i><i class="dot"></i><i class="dot"></i><i class="dot dot--off"></i><i class="dot dot--off"></i></span></li>
          <li class="profile__row"><span class="profile__name">BRIGHTNESS</span><span class="profile__scale"><i class="dot"></i><i class="dot"></i><i class="dot"></i><i class="dot dot--off"></i><i class="dot dot--off"></i></span></li>
        </ul>
      </div>
      <div class="facts">
        <div class="fact fact--weight"><div class="fact__title">WEIGHT</div><div class="fact__value">60 KG</div></div>
        <div class="facts__divider"></div>
        <div class="fact fact--date"><div class="fact__title">ROAST DATE</div><div class="fact__value">05/5/2021</div></div>
      </div>
      <div class="info__rule info__rule--bottom"></div>
    </div>
  </section>

</body>
</html>
```